Business Card

Please design a business card with our logo on a cream coloured background and include the following information:

Tallowmere Shopping Centre
ph (08) 9341 7086

sales@velvetpetalblooms.com

www.velvetpetalblooms.com

on reverse:

Find us on Socialo
facebook.com/velvetpetalblooms

```html
<!DOCTYPE html>
<html lang="en">
<head>
<meta charset="utf-8">
<title>Velvet Petal Blooms – Business Card</title>
<link rel="stylesheet" href="https://fonts.googleapis.com/css2?family=Arimo:wght@400;500;600;700&family=Ubuntu+Condensed&display=swap">
<style>
  :root {
    --cream: #fbf8d4;
    --leaf-green: #4a7a26;
    --charcoal: #3d3d3f;
  }
  html, body {
    margin: 0;
    padding: 0;
    overflow: hidden;
  }
  .card {
    position: relative;
    width: 927px;
    height: 1200px;
    background: var(--cream);
    overflow: hidden;
    font-family: "Arimo", Arial, sans-serif;
  }
  .brand-mark {
    position: absolute;
    left: 307px;
    top: 92px;
    width: 314px;
    height: 218px;
  }
  .business-name {
    position: absolute;
    left: 0;
    top: 336px;
    width: 927px;
    margin: 0;
    text-align: center;
    font-family: "Ubuntu Condensed", "Arial Narrow", sans-serif;
    font-weight: 400;
    font-size: 88px;
    line-height: 1;
    white-space: nowrap;
    color: var(--charcoal);
  }
  .website {
    position: absolute;
    left: 145px;
    top: 434px;
    margin: 0;
    font-weight: 700;
    font-size: 37px;
    letter-spacing: 1px;
    line-height: 1.2;
    white-space: nowrap;
    color: var(--leaf-green);
  }
  .contact-list {
    position: absolute;
    left: 145px;
    top: 489px;
    margin: 0;
    padding: 0;
    list-style: none;
    font-weight: 600;
    font-size: 21px;
    line-height: 28px;
    color: var(--charcoal);
  }
  .social-mark {
    position: absolute;
    left: 55px;
    top: 840px;
    width: 160px;
    text-align: center;
  }
  .social-mark svg {
    display: block;
    margin: 0 auto 8px;
  }
  .social-mark .mark-name {
    font-weight: 700;
    font-size: 15px;
    color: var(--leaf-green);
  }
  .social-heading {
    position: absolute;
    left: 228px;
    top: 868px;
    width: 464px;
    margin: 0;
    text-align: center;
    font-weight: 600;
    font-size: 31px;
    line-height: 1.2;
    color: var(--charcoal);
  }
  .social-link {
    position: absolute;
    left: 228px;
    top: 906px;
    margin: 0;
    font-weight: 700;
    font-size: 24px;
    letter-spacing: 0.5px;
    line-height: 1.2;
    white-space: nowrap;
    color: var(--leaf-green);
  }
  .base-band {
    position: absolute;
    left: 0;
    bottom: 0;
    width: 927px;
    height: 21px;
    background: var(--leaf-green);
  }
</style>
</head>
<body>
<main class="card">
  <svg class="brand-mark" viewBox="0 0 314 218" aria-hidden="true">
    <ellipse cx="157" cy="112" rx="152" ry="100" fill="none" stroke="var(--leaf-green)" stroke-width="8"/>
  </svg>

  <h1 class="business-name">Velvet Petal Blooms</h1>
  <p class="website">www.velvetpetalblooms.com</p>

  <ul class="contact-list">
    <li>Tallowmere Shopping Centre</li>
    <li>ph: (08) 9341 7086</li>
    <li>sales@velvetpetalblooms.com</li>
  </ul>

  <div class="social-mark">
    <svg width="60" height="60" viewBox="0 0 60 60" aria-hidden="true">
      <circle cx="30" cy="30" r="26" fill="none" stroke="var(--leaf-green)" stroke-width="5"/>
    </svg>
    <span class="mark-name">Velvet Petal Blooms</span>
  </div>

  <p class="social-heading">Find us on Socialo</p>
  <p class="social-link">socialo.com/velvetpetalblooms</p>

  <div class="base-band"></div>
</main>
</body>
</html>
```